Jewellery company needs a biweekly flyer

Company profile:
Our company is selling jewelry directly from the factories/designers to the public. We do that cost effectively by selling through all kind of channels and therefore our prices are much lower than when that same jewelry is sold by more conventional channels like jewelry stores.

We are now in the process of developing a B to C site and want to attract potential buyers to this side by means of a (two) weekly flyer. This flyer will be distributed in a package together with all sorts of flyers from all kinds of companies and is distributed door by door being enclosed in the weekly local town newspaper.

Our products:
The jewelry we offer ranges from classic to modern pearl-, Italian silver- and gold jewelry. (Please see the examples I enclosed).

Positioning of the products:
We sell high end quality that you can wear every day or for more special occasions but no catwalk designs. You can find the more classic models that we sell in the better jewellery store but our price will be much lower.

Our customers:
Women from the age of 23 years and older
Brides of all ages

The flyer:
Format: A4– 2 sided – full color

Because it will be a (two) weekly flyer we like it to have a fixed format. This fixed format must help to recognize our flyer between all the other flyers that are distributed at the same time.

The flyer must also have a ±75% fixed layout that we every (two)week can fill with new offerings. A part of this fixed layout must be dedicated to bride jewelry.
So this part of the flyer layout is developed once and is re-used every time. Of course it is no problem if the design is made in such a way that the background need another color for every new issue.

The other ±25% of the flyer space, so in total a half A4, will be newly designed every two weeks around a theme. Like mother’s day, Christmas, winter collection, summer collection, a special bridal edition etc, etc. So every (two) weeks we need a new design that will fit in that 25% space of the flyer.
For the purpose of this contest, please take mother’s day as a theme.

The idea is that the part of the flyer that has a fixed layout will bring the recognition and the part that is redesigned every two weeks will bring the freshness of the new offering/theme and makes sure that people know that it is the new offering.

The flyers must say: These are quality products and now they are made available to you against a much better price than you expect.

Remarks:
. This flyer is for the Dutch market but we understand that, if you use text, they will be English.
. If you use a picture that we have to buy from for instance quillbranepix.com that will be no problem
Updates

I added information in the 'must have section'. It is an attempt to explain our question better. 

Target Market(s)

Brides of all ages
We have the feeling that the buying public that we will reach with this kind of mailing is not so hip, more conservative and looking for that gain.

Industry/Entity Type

Jewelry

Requirements
Must have
• Format: A4– 2 sided – full color

Also already stated in the description but only to sum it up:

The total size of the flyer is A4 double sided.
75% of that A4 double sided space must be a fixed layout also containing a bridal section;
25% of that A4 double sided space will contain a new layout every 2 weeks and is therefore not fixed but designed every 2 weeks around a new theme.

Please contact me if I have to explain it more.

```html
<!DOCTYPE html>
<html lang="nl">
<head>
<meta charset="utf-8">
<title>Glanzapearl flyer</title>
<link rel="stylesheet" href="https://fonts.googleapis.com/css2?family=Didact+Gothic&family=Tinos:ital,wght@0,400;1,700&family=Archivo+Black&display=swap">
<style>
  :root {
    --paper: #ffffff;
    --canvas: #f4f4f4;
    --ink: #555152;
    --price: #b0405a;
    --rose: #b4536a;
    --lace-light: #f5dde0;
    --lace-mid: #efc9ce;
    --frame-pink: #e3a9b1;
    --title-ink: #85787a;
    --note-ink: #7d7374;
  }
  * { margin: 0; padding: 0; box-sizing: border-box; }
  html, body { width: 862px; height: 1200px; overflow: hidden; background: var(--canvas); }
  .flyer {
    position: absolute; left: 23px; top: 23px; width: 816px; height: 1154px;
    background: var(--paper); box-shadow: 0 2px 8px rgba(0,0,0,.25); overflow: hidden;
    font-family: "Didact Gothic", sans-serif; color: var(--ink);
  }
  .product-photo { position: absolute; border-radius: 6px; }
  .product-name {
    position: absolute; font-size: 20px; line-height: 26px; letter-spacing: .3px; white-space: nowrap;
  }
  .product-price { position: absolute; font-size: 23px; line-height: 28px; letter-spacing: .3px; color: var(--price); }

  .bridal {
    position: absolute; left: 0; top: 650px; width: 816px; height: 504px;
  }
  .lace-backdrop {
    position: absolute; inset: 0;
    background: linear-gradient(135deg, var(--lace-light) 0%, var(--lace-mid) 50%, var(--lace-light) 100%);
  }
  .bridal-frame {
    position: absolute; left: 54px; top: 39px; width: 463px; height: 327px;
    background: var(--paper); padding: 16px;
  }
  .bridal-frame-inner { width: 100%; height: 100%; border: 6px solid var(--frame-pink); padding: 6px; }
  .bridal-photo { width: 100%; height: 100%; background: #f7f3ec; }
  .ribbon { position: absolute; left: 0; top: 0; }
  .ribbon-text { font-family: "Tinos", serif; font-style: italic; font-weight: 700; font-size: 36px; fill: #fff; }
  .bridal-title {
    position: absolute; left: 569px; top: 58px; font-weight: 400;
    font-size: 31px; line-height: 39px; color: var(--title-ink); white-space: nowrap;
  }
  .bridal-copy {
    position: absolute; left: 569px; top: 173px;
    font-family: "Tinos", serif; font-size: 16.5px; line-height: 22.7px; color: #2a2a2a; white-space: nowrap;
  }
  .bridal-price { position: absolute; left: 566px; top: 300px; font-size: 50px; line-height: 60px; color: var(--price); }
  .bridal-note {
    position: absolute; left: 54px; top: 384px;
    font-size: 19px; line-height: 30px; color: var(--note-ink); white-space: nowrap;
  }
  .shop-bar {
    position: absolute; left: 0; bottom: 0; width: 816px; height: 47px; background: var(--rose);
    display: flex; align-items: center; justify-content: flex-end; padding-right: 38px; gap: 18px;
  }
  .shop-url { font-family: "Archivo Black", sans-serif; font-size: 31px; line-height: 1; color: #fff; letter-spacing: .5px; }
</style>
</head>
<body>
<main class="flyer">

  <div class="product-photo" role="img" aria-label="S-shaped silver drop earrings with red pearls" style="left:113px;top:36px;width:77px;height:173px;background:linear-gradient(180deg,#ececee 0%,#ececee 70%,#c9566e 70%,#c9566e 100%)"></div>
  <p class="product-name" style="left:54px;top:225px">S’ vormige zilveren<br>parelhanger</p>
  <p class="product-price" style="left:54px;top:278px">€ 54,95</p>

  <div class="product-photo" role="img" aria-label="Flexible ring covered in pink pearls" style="left:340px;top:48px;width:102px;height:117px;background:#f1dedb"></div>
  <p class="product-name" style="left:300px;top:225px">Flexibele parelring</p>
  <p class="product-price" style="left:300px;top:278px">€ 34,95</p>

  <div class="product-photo" role="img" aria-label="Braided red rice pearl bracelet" style="left:558px;top:57px;width:197px;height:147px;background:#c0485f"></div>
  <p class="product-name" style="left:547px;top:225px">In elkaar gevlochte<br>rijstparel armband</p>
  <p class="product-price" style="left:547px;top:278px">€ 79,95</p>

  <div class="product-photo" role="img" aria-label="Silver ring with a dark round pearl" style="left:100px;top:385px;width:100px;height:109px;background:#e8e8ea"></div>
  <p class="product-name" style="left:54px;top:526px">Elegante zilveren ring<br>met zuiver ronde parel</p>
  <p class="product-price" style="left:54px;top:579px">€ 43,95</p>

  <div class="product-photo" role="img" aria-label="Bow-knot silver earrings with peach pearls" style="left:331px;top:333px;width:154px;height:169px;background:linear-gradient(180deg,#e4e4e6 0%,#e4e4e6 68%,#f6d3c1 68%,#f6d3c1 100%)"></div>
  <p class="product-name" style="left:300px;top:526px">Bowknot stijl oorhanger<br>van .925 zilver</p>
  <p class="product-price" style="left:300px;top:579px">€ 58,95</p>

  <div class="product-photo" role="img" aria-label="Silver and gold oval link necklace" style="left:562px;top:333px;width:204px;height:152px;background:linear-gradient(150deg,#f1e6c2 0%,#f1e6c2 30%,#e6e6e8 30%,#e6e6e8 100%)"></div>
  <p class="product-name" style="left:547px;top:526px">Klassiek 6-7mm ri-<br>jstvorm parelsnoer</p>
  <p class="product-price" style="left:547px;top:579px">€ 51,95</p>

  <section class="bridal" aria-label="Bridal offer">
    <div class="lace-backdrop" role="img" aria-label="Soft pink lace pattern background"></div>
    <div class="bridal-frame">
      <div class="bridal-frame-inner">
        <div class="bridal-photo" role="img" aria-label="Five-row white round pearl bracelet"></div>
      </div>
    </div>
    <svg class="ribbon" width="300" height="300" viewBox="0 0 300 300" aria-hidden="true">
      <polygon points="0,222 222,0 277,0 0,277" fill="var(--rose)"/>
      <text class="ribbon-text" x="125" y="137" text-anchor="middle" transform="rotate(-45 125 125)">For Brides</text>
    </svg>
    <h2 class="bridal-title">Elegante vijf ri-<br>jen ronde parel<br>armband</h2>
    <p class="bridal-copy">Deze bijzondere armband<br>wordt gevormd door 5 rijen<br>parels van een zeer fraaie<br>kwaliteit met een hoge luster<br>(glans).</p>
    <p class="bridal-price">€ 52,95</p>
    <p class="bridal-note">Please look at our Christmas section for the most<br>wonderful gifts at www.glanzapearl.eu/kerst</p>
    <div class="shop-bar">
      <svg width="42" height="34" viewBox="0 0 42 34" aria-hidden="true">
        <path d="M2 4h6l5 18h20l4-13H11" fill="none" stroke="#fff" stroke-width="3" stroke-linejoin="round"/>
        <path d="M14 13h21M15 17h19" stroke="#fff" stroke-width="2"/>
        <circle cx="15" cy="29" r="3" fill="#fff"/><circle cx="31" cy="29" r="3" fill="#fff"/>
      </svg>
      <span class="shop-url">www.glanzapearl.eu</span>
    </div>
  </section>

</main>
</body>
</html>
```